Business Card Design Project

Company Name - Kestrova Care

Wellness consulting and training company. Run through a medical centre.

Main colour themes are orange and blue, as in the logo. Want to replicate same effect with business cards.

To give a sense of freedom and potential as per the company name.

Want the business card to be in line with stationary design, which I have launched as well.

Double sided with design and colour on one side and details on other side.
Updates

Reason: Need business card and stationary design to be teed up.

Target Market(s)

35 to 65 age group.
New age and trendy

Industry/Entity Type

Training

Requirements
Must have
• Colours orange and blue as per logo
Nice to have
• Design to be similar to stationary design, letterhead and envelopes

```html
<!DOCTYPE html>
<html lang="en">
<head>
<meta charset="utf-8">
<title>Kestrova Care — Stationery Set</title>
<link rel="stylesheet" href="https://fonts.googleapis.com/css2?family=Roboto+Condensed:wght@400&family=Open+Sans:wght@400;600&family=Cinzel:wght@500&display=swap">
<style>
  :root{
    --bg:#e8e9eb;
    --blue-deep:#0b57a8;
    --blue:#1f6fbf;
    --blue-light:#4a93d6;
    --orange:#f07a1e;
    --orange-light:#f6a257;
    --ink:#333a44;
    --muted:#6d7480;
    --paper:#ffffff;
  }
  *{box-sizing:border-box;margin:0;padding:0}
  html,body{width:1200px;height:1200px;overflow:hidden;background:var(--bg)}
  body{position:relative;font-family:"Open Sans",Arial,sans-serif;color:var(--ink)}
  .brand{font-family:"Roboto Condensed",Arial,sans-serif;font-weight:400;letter-spacing:.01em;white-space:nowrap}

  .sheet{position:absolute;top:96px;width:430px;height:604px;box-shadow:0 6px 18px rgba(0,0,0,.18)}

  /* Folder cover */
  .cover{left:186px;background:linear-gradient(90deg,var(--blue-deep) 0%,var(--blue) 55%,var(--blue-light) 100%)}
  .cover .brand{position:absolute;top:92px;left:0;width:100%;text-align:center;color:#fff;font-size:27px}

  /* Letterhead */
  .letterhead{left:646px;background:var(--paper);font-size:8.4px;line-height:1.5}
  .letterhead .brand{position:absolute;top:52px;left:0;width:100%;text-align:center;color:var(--blue);font-size:21px}
  .letter-body{position:absolute;top:142px;left:45px;width:340px}
  .recipient{margin-bottom:14px}
  .letter-body p{margin-bottom:10px;text-align:justify}
  .signoff{margin-top:4px}
  .signature-row{display:flex;align-items:center;gap:8px;margin-top:22px}
  .signature{width:56px;height:20px;background:linear-gradient(90deg,#6a5aa8,#8e82c2);opacity:.55;border-radius:10px}
  .seal{width:30px;height:30px;border-radius:50%;border:2px solid #7fc6c4;opacity:.8}

  .letter-footer{position:absolute;left:0;bottom:0;width:100%;height:34px}
  .letter-footer .band{position:absolute;inset:0;background:linear-gradient(90deg,var(--blue-deep),var(--blue-light))}
  .letter-footer .accent{position:absolute;right:0;top:0;height:14px;width:168px;background:var(--orange);clip-path:polygon(10% 0,100% 0,100% 100%,0 100%)}
  .letter-footer .accent span{position:absolute;right:8px;top:2px;font-size:7px;letter-spacing:.06em;color:#fff;text-transform:uppercase}
  .contact-list{position:absolute;left:14px;top:3px;list-style:none;color:#fff;font-size:6.6px;line-height:9.5px;letter-spacing:.05em;text-transform:uppercase}
  .contact-list li{display:flex;align-items:center;gap:5px}
  .contact-list svg{width:7px;height:7px}

  /* Business cards */
  .card{position:absolute;top:800px;width:480px;height:274px;box-shadow:0 6px 16px rgba(0,0,0,.2);overflow:hidden}

  .card-details{left:84px;background:var(--paper)}
  .card-details .brand{position:absolute;top:30px;right:34px;color:var(--blue);font-size:26px}
  .card-details .address-strip{position:absolute;top:92px;right:0;width:250px;height:28px;background:linear-gradient(90deg,var(--orange-light),var(--orange));clip-path:polygon(8% 0,100% 0,100% 100%,0 100%)}
  .card-details .address-strip span{position:absolute;right:18px;top:8px;font-size:8.5px;letter-spacing:.12em;color:#fff;text-transform:uppercase}
  .card-details .person{position:absolute;left:30px;top:112px}
  .person-name{font-family:"Cinzel",Georgia,serif;font-weight:500;font-size:17px;color:var(--blue);letter-spacing:.04em}
  .person-role{font-size:9px;letter-spacing:.16em;color:var(--orange);text-transform:uppercase;margin-top:2px}
  .card-details .contact-list{position:static;color:var(--muted);font-size:8px;line-height:13px;letter-spacing:.08em}
  .card-details .contact-list svg{width:9px;height:9px}
  .card-details .contacts{position:absolute;left:30px;top:168px}
  .card-details .wave{position:absolute;left:0;bottom:0;width:100%;height:64px;background:linear-gradient(90deg,var(--blue-light),var(--blue-deep));clip-path:polygon(0 55%,62% 10%,100% 0,100% 100%,0 100%)}

  .card-front{left:636px;background:linear-gradient(135deg,var(--blue-deep) 0%,var(--blue) 45%,#5aa6e0 100%)}
  .card-front .brand{position:absolute;top:50%;left:0;width:100%;text-align:center;transform:translateY(-50%);color:#fff;font-size:44px}
  .card-front .edge{position:absolute;left:0;bottom:0;width:100%;height:8px;background:var(--orange)}
</style>
</head>
<body>

<section class="sheet cover" aria-label="Presentation folder cover">
  <div class="brand">Kestrova Care</div>
</section>

<section class="sheet letterhead" aria-label="Letterhead">
  <div class="brand">Kestrova Care</div>
  <div class="letter-body">
    <div class="recipient">Mara Ellison<br>24 Harbour Rd<br>Fenwick</div>
    <p>Dear Mara Ellison,</p>
    <p>Thank you for your interest in our wellness programs. Our team of consultants works alongside the medical centre to design training that fits your goals, your schedule and your pace of life.</p>
    <p>Each program begins with a short assessment, followed by guided sessions and regular reviews. We keep every plan flexible so progress stays steady and realistic.</p>
    <p>We look forward to meeting you and helping you reach your full potential. Please contact our office to arrange a first consultation at a time that suits you.</p>
    <div class="signoff">Your Sincerely,<br>Tomas Reyne.</div>
    <div class="signature-row">
      <div class="signature" role="img" aria-label="Handwritten signature"></div>
      <div class="seal" role="img" aria-label="Company seal"></div>
    </div>
  </div>
  <footer class="letter-footer">
    <div class="band"></div>
    <div class="accent"><span>Here your companyor home address</span></div>
    <ul class="contact-list">
      <li><svg viewBox="0 0 10 10"><path d="M2 1h2l1 2-1 1a5 5 0 0 0 2 2l1-1 2 1v2c-4 0-7-3-7-7z" fill="#fff"/></svg>+88 612 300 41</li>
      <li><svg viewBox="0 0 10 10"><rect x="1" y="2" width="8" height="6" fill="none" stroke="#fff"/><path d="M1 2l4 3 4-3" fill="none" stroke="#fff"/></svg>info@kestrovacare.com</li>
      <li><svg viewBox="0 0 10 10"><rect x="1" y="1.5" width="8" height="5.5" fill="none" stroke="#fff"/><path d="M3 9h4M5 7v2" stroke="#fff"/></svg>www.kestrovacare.com</li>
    </ul>
  </footer>
</section>

<section class="card card-details" aria-label="Business card, details side">
  <div class="brand">Kestrova Care</div>
  <div class="address-strip"><span>Here your companyor home address</span></div>
  <div class="person">
    <div class="person-name">Elin Carver</div>
    <div class="person-role">Manager</div>
  </div>
  <div class="contacts">
    <ul class="contact-list">
      <li><svg viewBox="0 0 10 10"><path d="M2 1h2l1 2-1 1a5 5 0 0 0 2 2l1-1 2 1v2c-4 0-7-3-7-7z" fill="#1f6fbf"/></svg>+88 612 300 41</li>
      <li><svg viewBox="0 0 10 10"><rect x="1" y="2" width="8" height="6" fill="none" stroke="#1f6fbf"/><path d="M1 2l4 3 4-3" fill="none" stroke="#1f6fbf"/></svg>info@kestrovacare.com</li>
      <li><svg viewBox="0 0 10 10"><rect x="1" y="1.5" width="8" height="5.5" fill="none" stroke="#1f6fbf"/><path d="M3 9h4M5 7v2" stroke="#1f6fbf"/></svg>www.kestrovacare.com</li>
    </ul>
  </div>
  <div class="wave"></div>
</section>

<section class="card card-front" aria-label="Business card, brand side">
  <div class="brand">Kestrova Care</div>
  <div class="edge"></div>
</section>

</body>
</html>
```